依頼概要
新発売する「大粒こがね山里だれ煮」の商品ラベルのデザインを募集いたします。
こちらの商品は追加依頼する予定の「薄切りこがね山椒煮」と姉妹商品であり、
デザイン決定された方には追加で依頼(1.2万円)させていただきます。今後商品を拡充することも検討中です。

◆会社概要
当社は創業明治30年という老舗企業です。国産の干し椎茸の卸問屋であり、
今後は当社の干し椎茸を使用した加工品の販売にも力を入れていく予定です。
会社の概要についてはHPを参照ください。
www.minasesangyo.jp

◆商品ラベルについて
ラベルサイズ:横55ミリ×縦85ミリ(角丸)
※大量生産できるまでは、光沢無地シールを使用、カラーインクジェットプリンターで印刷する予定です。
商品サイズ :横150ミリ×縦210ミリ×厚10ミリ(袋のサイズ)

◆商品イメージ
椎茸屋が販売する椎茸の加工品であることが売りです。
一般的な加工品は中国産の安い椎茸を使っているケースが多いのですが、安心安全な国産椎茸が原料となっています。
販売価格は150gで500~600円を想定。少々高目ですが、本物の味、美味しさをアピールできればと思います。
販売先は土産店、道の駅などとなります。店頭には漬物などの加工品がたくさん置かれていますので、いいデザインで存在感を出したいものです。
椎茸が黒、あるいはこげ茶色ですので、ラベル事態は白ベースかと思います。
田舎っぽいシンプルなデザインが希望です。
椎茸のイラストなどが入るといいと思います。

◆掲載文字について
商品名:大粒こがね山里だれ煮
そのほかの文字:国産・原木椎茸を使用
会社名:ミナセ産業株式会社(ロゴを使用)
※何かキャッチコピーを入れてもよい

よいご提案をお待ちしております!!
このたびは弊社の商品ラベルデザインのコンペにご応募いただき、ありがとうございました。選考の結果、選定者を確定させていただきました。選定者には直接、メールにてご連絡させていただいております。たくさんのご応募ありがとうございました!

全体の雰囲気と椎茸のイラストがとても気に入りました。
修正依頼にも手早く対応いただき、たいへん助かりました。

たくさんのご提案ありがとうございました!
初めての依頼でしたので不手際もあったかと思いますが、
力作が集まって選考に苦戦しました。
今後ともよろしくお願いいたします。

```html
<!DOCTYPE html>
<html lang="ja">
<head>
<meta charset="utf-8">
<title>大粒こがね山里だれ煮 商品ラベル</title>
<link rel="stylesheet" href="https://fonts.googleapis.com/css2?family=Yuji+Boku&family=Noto+Serif+JP:wght@500;700&display=swap">
<style>
:root{
  --page:#f4f1ec;
  --frame:#e0761c;
  --frame-dark:#b9550f;
  --paper:#fffaf1;
  --ink:#1c120c;
  --brown:#5a3214;
  --mush-cap:#7a4622;
  --mush-stem:#d9b98a;
}
*{margin:0;padding:0;box-sizing:border-box}
html,body{width:879px;height:1200px;overflow:hidden;background:var(--page)}
.label{
  position:absolute;left:140px;top:137px;width:600px;height:927px;
  background:var(--frame);border-radius:48px;padding:26px;
}
.label__inner{
  position:relative;width:100%;height:100%;
  background:var(--paper);border-radius:30px;overflow:hidden;
}
.name{
  position:absolute;left:30px;top:40px;width:330px;
  font-family:"Yuji Boku",serif;font-weight:400;color:var(--ink);line-height:1;
}
.name__lead{display:block;font-size:56px;color:var(--brown);margin-left:8px}
.name__main{display:block;font-size:108px;letter-spacing:-2px;margin-top:20px;white-space:nowrap}
.name__sub{display:block;font-size:108px;letter-spacing:-2px;margin-top:22px;line-height:1.1;white-space:nowrap}
.claim{
  position:absolute;right:28px;top:40px;height:240px;writing-mode:vertical-rl;
  font-family:"Noto Serif JP",serif;font-weight:700;font-size:30px;line-height:1.5;
  color:var(--brown);letter-spacing:4px;
}
.illustration{position:absolute;right:28px;top:310px;width:140px;height:280px}
.maker{
  position:absolute;left:0;right:0;bottom:0;height:150px;
  border-top:4px solid var(--frame);display:flex;align-items:center;gap:20px;padding:0 36px;
}
.maker__mark{width:56px;height:56px;border-radius:50%;background:var(--frame-dark);flex:none}
.maker__text{font-family:"Noto Serif JP",serif;color:var(--ink)}
.maker__name{font-weight:700;font-size:36px;letter-spacing:2px}
.maker__addr{font-weight:500;font-size:16px;color:var(--brown);margin-top:6px}
</style>
</head>
<body>
<div class="label">
  <div class="label__inner">
    <h1 class="name">
      <span class="name__lead">大粒</span>
      <span class="name__main">こがね</span>
      <span class="name__sub">山里<br>だれ煮</span>
    </h1>
    <p class="claim">信州産の<br>原木椎茸を<br>使っています</p>
    <svg class="illustration" role="img" aria-label="椎茸のイラスト" viewBox="0 0 140 280" preserveAspectRatio="none">
      <defs>
        <linearGradient id="mushroomTone" x1="0" y1="0" x2="0" y2="1">
          <stop offset="0" stop-color="#7a4622"/>
          <stop offset="1" stop-color="#d9b98a"/>
        </linearGradient>
      </defs>
      <rect width="140" height="280" rx="20" fill="url(#mushroomTone)"/>
    </svg>
    <div class="maker">
      <span class="maker__mark"></span>
      <div class="maker__text">
        <p class="maker__name">ミナセ産業株式会社</p>
        <p class="maker__addr">長野県中野市 www.minasesangyo.jp</p>
      </div>
    </div>
  </div>
</div>
</body>
</html>
```